postcard design for moving company

Bramwell  Movers and Storage -moving company , we send postcards to potential clients that have their houses for sale. Must be a postard that is easy to read , where you can notice some deals, reason not to throw the card to junk.
family owned and operated company.
Free estimate
Flat Rate , license and insured, then we must put the zindle and vork 5 stars.
coupons:
$50 Off for all long distance moving
1 month Free Storage for out of state moves.
5% Off for seniors nd veterans.

```html
<!DOCTYPE html>
<html lang="en">
<head>
<meta charset="utf-8">
<title>Bramwell Movers and Storage – Postcard</title>
<link rel="stylesheet" href="https://fonts.googleapis.com/css2?family=Montserrat:wght@400;500;600;700;800&display=swap">
<style>
  :root {
    --coral: #e85f61;
    --coral-deep: #d9474b;
    --charcoal: #2e3236;
    --stage: #3d3d3d;
    --panel-light: #f4f4f5;
    --panel-mid: #d6d7d9;
    --white: #ffffff;
    --gold: #f5b31c;
    --rule: #6b6e72;
  }
  * { margin: 0; padding: 0; box-sizing: border-box; }
  html, body {
    width: 829px; height: 1200px; overflow: hidden;
    background: var(--stage);
    font-family: "Montserrat", Arial, sans-serif;
  }
  .postcard {
    position: absolute; left: 57px; width: 716px; height: 517px;
    filter: drop-shadow(4px 6px 6px rgba(0,0,0,.45));
  }
  .postcard--front { top: 50px; }
  .postcard--back { top: 617px; }
  .postcard svg { display: block; width: 716px; height: 517px; }
  .brand-name { font-weight: 500; fill: var(--white); }
  .headline { font-weight: 800; fill: var(--white); }
  .subline { font-weight: 400; fill: var(--white); }
  .offer-title { font-weight: 800; fill: var(--charcoal); }
  .offer-accent { fill: var(--coral); }
  .offer-note { font-weight: 500; fill: var(--charcoal); }
  .rating-name { font-weight: 600; fill: var(--white); }
  .contact-phone { font-weight: 700; }
  .contact-mail { font-weight: 400; }
  .on-coral { fill: var(--white); }
  .on-light { fill: var(--charcoal); }
</style>
</head>
<body>

<div class="postcard postcard--front">
  <svg viewBox="0 0 716 517" xmlns="http://www.w3.org/2000/svg">
    <defs>
      <linearGradient id="offer-panel" x1="0" y1="0" x2="1" y2="0">
        <stop offset="0" stop-color="#c9cacc"/>
        <stop offset=".35" stop-color="var(--panel-light)"/>
        <stop offset=".8" stop-color="var(--panel-mid)"/>
      </linearGradient>
      <linearGradient id="truck-photo" x1="0" y1="0" x2="1" y2="1">
        <stop offset="0" stop-color="#e9eaea"/>
        <stop offset=".35" stop-color="#8b8f8f"/>
        <stop offset=".5" stop-color="#2b2f31"/>
        <stop offset="1" stop-color="#1f2325"/>
      </linearGradient>
    </defs>

    <rect class="card-base" width="716" height="517" fill="var(--charcoal)"/>
    <polygon class="accent-strip" points="0,134 185,134 185,146 0,160" fill="var(--coral)"/>
    <polygon class="offer-panel" points="0,160 716,121 716,440 262,418 0,441" fill="url(#offer-panel)"/>
    <polygon class="truck-photo" role="img" aria-label="Photo of a white moving truck with a dark branded box body"
             points="320,146 716,121 716,440 320,440" fill="url(#truck-photo)"/>
    <polygon class="headline-band" points="346,0 716,0 716,96 357,128" fill="var(--coral)"/>
    <polygon class="headline-band-edge" points="530,122 716,96 716,122" fill="var(--white)"/>
    <polygon class="contact-band" points="262,443 716,402 716,517 269,517" fill="var(--coral)"/>

    <g class="brand">
      <text class="brand-name" x="31" y="64" font-size="33">bramwell movers</text>
      <text class="brand-name" x="160" y="92" font-size="19">&amp; storage</text>
    </g>

    <text class="headline" x="392" y="63" font-size="36">Free estimate</text>
    <text class="subline" x="393" y="86" font-size="16.5">Flat Rate , license and insured</text>

    <g class="offers">
      <text class="offer-title" x="31" y="196" font-size="27"><tspan class="offer-accent">$50</tspan> OFF</text>
      <text class="offer-note" x="31" y="216" font-size="15.5">for all long distance moving</text>
      <rect x="31" y="231" width="131" height="3.5" fill="var(--charcoal)"/>
      <text class="offer-title offer-accent" x="31" y="275" font-size="27">1 MONTH</text>
      <text class="offer-title" x="31" y="308" font-size="27">FREE STORAGE</text>
      <text class="offer-note" x="31" y="328" font-size="15.5">for out of state moves.</text>
      <rect x="31" y="347" width="131" height="3.5" fill="var(--charcoal)"/>
      <text class="offer-title" x="31" y="388" font-size="27"><tspan class="offer-accent">5%</tspan> OFF</text>
      <text class="offer-note" x="31" y="407" font-size="15.5">for seniors and veterans.</text>
    </g>

    <g class="ratings">
      <g class="stars" fill="var(--gold)">
        <text x="33" y="466" font-size="14" letter-spacing="1">★★★★★</text>
      </g>
      <text class="rating-name" x="31" y="489" font-size="21">zindle</text>
      <text class="rating-name" x="133" y="474" font-size="21">vork</text>
      <rect x="133" y="479" width="73" height="14" fill="var(--coral-deep)"/>
      <text x="135" y="491" font-size="12" fill="var(--white)" letter-spacing="1.5">★★★★★</text>
    </g>

    <g class="contact">
      <circle cx="438" cy="449" r="10" fill="none" stroke="var(--white)" stroke-width="1.6"/>
      <path d="M434.5 444.5c1-1 2-.5 2.5.6l.6 1.4c.2.6-.2 1.1-.7 1.5.6 1.5 1.7 2.6 3.2 3.2.4-.5.9-.9 1.5-.7l1.4.6c1.1.5 1.6 1.5.6 2.5-3.7 2.5-11.6-5.4-9.1-9.1z" fill="var(--white)"/>
      <text class="contact-phone on-coral" x="461" y="461" font-size="28">212-555-0147</text>
      <circle cx="438" cy="482" r="10" fill="none" stroke="var(--white)" stroke-width="1.6"/>
      <rect x="432.5" y="478" width="11" height="8" fill="var(--white)"/>
      <path d="M432.5 478l5.5 4.5 5.5-4.5" fill="none" stroke="var(--coral)" stroke-width="1"/>
      <text class="contact-mail on-coral" x="461" y="492" font-size="21" textLength="218" lengthAdjust="spacingAndGlyphs">hello@bramwell.com</text>
    </g>
  </svg>
</div>

<div class="postcard postcard--back">
  <svg viewBox="0 0 716 517" xmlns="http://www.w3.org/2000/svg">
    <defs>
      <linearGradient id="address-panel" x1="0" y1="0" x2="1" y2="1">
        <stop offset="0" stop-color="#c8c9cb"/>
        <stop offset=".5" stop-color="var(--panel-light)"/>
        <stop offset=".75" stop-color="#e4e5e6"/>
        <stop offset="1" stop-color="#cfd0d2"/>
      </linearGradient>
      <linearGradient id="skyline-photo" x1="0" y1="0" x2="0" y2="1">
        <stop offset="0" stop-color="#dfe3e8"/>
        <stop offset=".35" stop-color="#e8dccf"/>
        <stop offset=".65" stop-color="#8d939b"/>
        <stop offset="1" stop-color="#3c424a"/>
      </linearGradient>
      <linearGradient id="crew-photo" x1="0" y1="0" x2="1" y2="0">
        <stop offset="0" stop-color="#b9b4a6"/>
        <stop offset=".4" stop-color="#3a3e42"/>
        <stop offset=".75" stop-color="#c9a882"/>
        <stop offset="1" stop-color="#2a2d31"/>
      </linearGradient>
    </defs>

    <rect class="card-base" width="716" height="517" fill="var(--charcoal)"/>
    <polygon class="accent-strip" points="0,105 185,105 185,118 0,131" fill="var(--coral)"/>
    <polygon class="skyline-photo" role="img" aria-label="Aerial photo of the city skyline at dusk"
             points="0,131 387,97 403,294 0,325" fill="url(#skyline-photo)"/>
    <polygon class="crew-photo" role="img" aria-label="Photo of the moving crew carrying boxes beside the truck"
             points="0,351 403,318 419,517 0,517" fill="url(#crew-photo)"/>
    <polygon class="top-band" points="377,0 716,0 716,22 383,51" fill="var(--coral)"/>
    <polygon class="address-panel" points="383,51 716,22 716,440 420,467" fill="url(#address-panel)"/>
    <polygon class="bottom-band" points="420,467 716,440 716,517 420,517" fill="var(--coral)"/>

    <g class="brand">
      <text class="brand-name" x="45" y="58" font-size="31">bramwell movers</text>
      <text class="brand-name" x="183" y="86" font-size="18">&amp; storage</text>
    </g>

    <rect class="stamp-box" x="614" y="52" width="68" height="68" fill="none" stroke="var(--rule)" stroke-width="1"/>
    <g class="address-lines" stroke="var(--rule)" stroke-width="1">
      <line x1="412" y1="180" x2="681" y2="180"/>
      <line x1="412" y1="231" x2="681" y2="231"/>
      <line x1="412" y1="283" x2="681" y2="283"/>
    </g>

    <g class="contact">
      <circle cx="444" cy="378" r="11" fill="none" stroke="var(--coral)" stroke-width="1.6"/>
      <path d="M440.5 373.5c1-1 2-.5 2.5.6l.6 1.4c.2.6-.2 1.1-.7 1.5.6 1.5 1.7 2.6 3.2 3.2.4-.5.9-.9 1.5-.7l1.4.6c1.1.5 1.6 1.5.6 2.5-3.7 2.5-11.6-5.4-9.1-9.1z" fill="var(--charcoal)"/>
      <text class="contact-phone on-light" x="470" y="391" font-size="28">212-555-0147</text>
      <circle cx="444" cy="412" r="11" fill="none" stroke="var(--coral)" stroke-width="1.6"/>
      <rect x="438.5" y="408" width="11" height="8" fill="var(--charcoal)"/>
      <path d="M438.5 408l5.5 4.5 5.5-4.5" fill="none" stroke="var(--panel-light)" stroke-width="1"/>
      <text class="contact-mail on-light" x="470" y="422" font-size="21" textLength="218" lengthAdjust="spacingAndGlyphs">hello@bramwell.com</text>
    </g>
  </svg>
</div>

</body>
</html>
```